Flyer for Cool Choir Concert

8.5x11 color flyer, to get people to attend excellent concert

Requirements
Should not have
• I don't like a lot of musical symbols incorporated into the design.

```html
<!DOCTYPE html>
<html lang="en">
<head>
<meta charset="utf-8">
<title>War and Peace – Concert Flyer</title>
<link href="https://fonts.googleapis.com/css2?family=Tinos:wght@400;700&family=Stardos+Stencil:wght@700&display=swap" rel="stylesheet">
<style>
  :root {
    --purple: #4a1670;
    --parchment-light: #d9b874;
    --parchment: #c49a52;
    --parchment-dark: #8e6630;
    --copper: #c4823f;
    --copper-light: #d9a062;
    --ink: #2b1a0c;
    --ink-brown: #3d2611;
    --white: #ffffff;
    --grey-text: #333333;
    --lilac: #e9dff2;
  }
  * { box-sizing: border-box; margin: 0; padding: 0; }
  html, body { width: 707px; height: 1200px; overflow: hidden; }
  body { font-family: "Tinos", "Times New Roman", serif; background: var(--white); }

  .flyer {
    position: relative;
    width: 707px;
    height: 1200px;
    overflow: hidden;
    background: radial-gradient(ellipse at 50% 45%, var(--parchment-light) 0%, var(--parchment) 55%, var(--parchment-dark) 100%);
  }

  .header-band { position: absolute; left: 0; top: 0; width: 707px; height: 190px; }
  .header-text { position: absolute; left: 0; top: 22px; width: 707px; text-align: center; color: var(--white); }
  .header-text .ensemble { font-weight: 700; font-size: 38px; letter-spacing: 1px; line-height: 44px; }
  .header-text .tagline { font-size: 24px; line-height: 33px; color: #f3ecf8; margin-top: 4px; }

  .concert-title { position: absolute; left: 0; top: 205px; width: 707px; text-align: center; }
  .concert-title .presents { font-weight: 700; font-size: 33px; color: var(--ink-brown); letter-spacing: 1px; line-height: 40px; }
  .concert-title .program { font-family: "Stardos Stencil", "Tinos", serif; font-weight: 700; font-size: 62px; color: var(--purple); letter-spacing: 2px; line-height: 66px; }
  .concert-blurb { position: absolute; left: 92px; top: 340px; width: 523px; text-align: center; font-size: 14px; line-height: 17px; color: var(--ink); }

  .choir-photo { position: absolute; left: 78px; top: 396px; width: 552px; height: 384px; }

  .lower-wave { position: absolute; left: 0; top: 790px; width: 707px; height: 410px; }

  .venue { position: absolute; left: 10px; top: 966px; width: 336px; text-align: center; }
  .venue .ensemble-name { font-weight: 700; font-size: 38px; color: var(--purple); letter-spacing: 1px; line-height: 44px; }
  .venue .place { font-weight: 700; font-size: 17px; line-height: 26px; color: var(--grey-text); margin-top: 30px; }
  .venue .web { display: flex; align-items: center; gap: 8px; margin-top: 14px; font-weight: 700; font-size: 18px; color: var(--purple); }
  .venue .web::before, .venue .web::after { content: ""; flex: 1; height: 1px; background: #8a8a8a; }
  .venue .note { font-weight: 700; font-size: 10.5px; color: var(--grey-text); margin-top: 2px; }

  .divider { position: absolute; left: 356px; top: 912px; width: 1px; height: 258px; background: #777; }

  .dates { position: absolute; left: 372px; top: 904px; width: 312px; }
  .date-pill {
    height: 38px; margin-bottom: 19px; border-radius: 19px;
    background: linear-gradient(180deg, var(--copper-light), var(--copper));
    color: var(--ink); font-weight: 700; font-size: 18.5px; text-align: center; line-height: 38px;
  }
  .ticket-note { position: absolute; left: 372px; top: 1016px; width: 312px; text-align: center; font-weight: 700; font-size: 12.5px; line-height: 17px; color: var(--ink); }

  .ticket { position: absolute; left: 438px; top: 1064px; width: 225px; height: 120px; }
  .ticket svg { position: absolute; left: 0; top: 0; }
  .ticket .prices { position: absolute; left: 0; top: 14px; width: 225px; text-align: center; color: var(--lilac); font-size: 23px; line-height: 30px; }
</style>
</head>
<body>
<main class="flyer">

  <svg class="header-band" viewBox="0 0 707 190" aria-hidden="true">
    <path fill="#efe6d2" d="M0,0 H707 V172 L690,166 L672,176 L650,168 L628,178 L604,169 L582,179 L556,170 L532,180 L508,171 L486,181 L460,172 L436,182 L410,173 L388,183 L362,174 L338,182 L312,172 L288,181 L262,171 L238,180 L214,170 L190,178 L166,169 L140,177 L116,167 L92,175 L68,166 L44,174 L20,165 L0,171 Z"/>
    <path fill="var(--purple)" d="M0,0 H707 V166 L690,160 L672,170 L650,161 L628,172 L604,162 L582,173 L556,163 L532,174 L508,164 L486,175 L460,165 L436,176 L410,166 L388,177 L362,167 L338,176 L312,165 L288,175 L262,164 L238,174 L214,163 L190,172 L166,162 L140,171 L116,160 L92,169 L68,159 L44,168 L20,158 L0,164 Z"/>
  </svg>

  <header class="header-text">
    <div class="ensemble">HARMONIA</div>
    <div class="tagline">Choral Artists of the High Desert Daniel Corwin,<br>Artistic Director</div>
  </header>

  <section class="concert-title">
    <div class="presents">PRESENTS</div>
    <h1 class="program">WAR AND PEACE</h1>
  </section>

  <p class="concert-blurb">Join the singers of Harmonia as we perform music borne out of warfare and conflict, and music that celebrates peace and love. Featuring music of Aaron Whitley, Helen Marsh, Owen Tate, Clara Benton, and others.</p>

  <svg class="choir-photo" viewBox="0 0 552 384" role="img" aria-label="Photo of the choir in black concert dress standing on risers, with a conductor at a grand piano">
    <defs>
      <linearGradient id="photoTone" x1="0" y1="0" x2="0" y2="1">
        <stop offset="0" stop-color="#d7a950"/>
        <stop offset="0.45" stop-color="#8a6a44"/>
        <stop offset="1" stop-color="#3a3028"/>
      </linearGradient>
    </defs>
    <path fill="#ffffff" d="M6,10 L40,2 L80,8 L120,0 L170,7 L220,1 L270,9 L320,2 L370,8 L420,0 L470,7 L520,2 L548,9 L544,60 L552,110 L545,170 L551,230 L544,290 L550,340 L546,380 L500,374 L450,382 L400,375 L350,383 L300,376 L250,384 L200,377 L150,383 L100,375 L50,382 L4,376 L9,320 L1,260 L8,200 L0,140 L7,80 L0,40 Z"/>
    <path fill="url(#photoTone)" d="M16,20 L60,14 L110,19 L160,12 L210,18 L260,13 L310,19 L360,13 L410,18 L460,12 L510,18 L536,16 L532,80 L538,150 L532,220 L537,290 L533,366 L480,361 L420,367 L360,361 L300,368 L240,362 L180,368 L120,361 L60,367 L16,363 L20,300 L13,230 L19,160 L13,90 L18,50 Z"/>
  </svg>

  <svg class="lower-wave" viewBox="0 0 707 410" aria-hidden="true">
    <path fill="var(--purple)" d="M0,77 C220,120 480,80 707,13 L707,56 C480,112 240,150 0,141 Z"/>
    <path fill="var(--white)" d="M0,141 C240,150 480,112 707,56 V410 H0 Z"/>
  </svg>

  <section class="venue">
    <div class="ensemble-name">HARMONIA</div>
    <div class="place">Grace Hill Community Church<br>1840 Mesa Verde Avenue NE Riverton</div>
    <div class="web">www.harmonia-choir.org</div>
    <div class="note">Complimentary childcare provided at both performances.</div>
  </section>

  <div class="divider"></div>

  <section class="dates">
    <div class="date-pill">Saturday, October 13 at 7:30pm</div>
    <div class="date-pill">Sunday, October 14 at 3:00pm</div>
  </section>

  <p class="ticket-note">Tickets Available Online<br>and at The Door</p>

  <div class="ticket">
    <svg width="225" height="120" viewBox="0 0 225 120" aria-hidden="true">
      <path fill="var(--purple)" d="M12,0 H213 A12,12 0 0 0 225,12 V108 A12,12 0 0 0 213,120 H12 A12,12 0 0 0 0,108 V12 A12,12 0 0 0 12,0 Z"/>
      <path fill="none" stroke="var(--lilac)" stroke-width="1.2" stroke-dasharray="3 2" d="M16,6 H209 A12,12 0 0 0 219,16 V104 A12,12 0 0 0 209,114 H16 A12,12 0 0 0 6,104 V16 A12,12 0 0 0 16,6 Z"/>
    </svg>
    <div class="prices">General $20<br>Seniors $15<br>Students $10</div>
  </div>

</main>
</body>
</html>
```